Gratulation zur Firmengründung
Zielgruppe
Wir sind eine Steuerberatungskanzlei. Das Design soll potentiellen Neukunden gefallen!
Aufgabenstellung
Wir möchten einen Flyer im Format 21x9,8 erstellen. Eine Skizzierung der Idee findet sich in der angefügten Datei.

```html
<!DOCTYPE html>
<html lang="de">
<head>
<meta charset="utf-8">
<title>Gratulation zur Firmengründung – Flyer</title>
<link rel="stylesheet" href="https://fonts.googleapis.com/css2?family=Crimson+Pro:ital,wght@0,400;1,400&family=Sorts+Mill+Goudy&family=Arimo&display=swap">
<style>
  :root {
    --green: #659a1c;
    --green-text: #5f9420;
    --ink: #111111;
    --paper: #ffffff;
    --backdrop: #dedede;
    --tablet-dark: #121416;
    --cork: #b08a5c;
  }
  * { margin: 0; padding: 0; box-sizing: border-box; }
  html, body { width: 1200px; height: 1200px; overflow: hidden; background: var(--backdrop); }
  .stage { position: relative; width: 1200px; height: 1200px; }

  .flyer {
    position: absolute; left: 114px; width: 972px; height: 452px;
    background: var(--paper); overflow: hidden;
  }
  .flyer--front { top: 96px; }
  .flyer--back { top: 578px; }

  .headline { font-family: "Crimson Pro", Georgia, serif; font-style: italic; font-weight: 400; color: var(--green-text); position: absolute; line-height: 1; white-space: nowrap; }
  .headline__we { left: 46px; top: 84px; font-size: 82px; }
  .headline__congrats { left: 142px; top: 150px; font-size: 44px; }
  .headline__founding { left: 44px; top: 186px; font-size: 80px; }

  .band {
    position: absolute; left: 0; top: 347px; width: 585px; height: 69px;
    background: var(--green); color: var(--paper);
  }
  .band__question {
    font-family: "Crimson Pro", Georgia, serif; font-style: italic; font-size: 32px;
    position: absolute; left: 47px; top: 14px; white-space: nowrap;
  }
  .band__contact {
    font-family: "Sorts Mill Goudy", Georgia, serif; font-size: 15.5px; line-height: 21px;
    position: absolute; top: 14px; left: 0; width: 100%;
  }
  .band__address { position: absolute; left: 46px; width: 160px; white-space: nowrap; }
  .band__reach { position: absolute; left: 203px; width: 380px; white-space: nowrap; }

  .photo { position: absolute; }
  .photo--cork-front {
    left: 580px; top: 88px; width: 370px; height: 258px;
    background: radial-gradient(ellipse at 60% 55%, var(--cork) 0%, #c9ab82 45%, #f2efe9 75%, var(--paper) 100%);
  }

  .brand { position: absolute; left: 643px; top: 350px; width: 280px; background: var(--paper); }
  .brand--back { left: 640px; top: 344px; width: 296px; padding: 6px 8px 8px; }
  .brand__name { font-family: "Crimson Pro", Georgia, serif; font-size: 37px; color: var(--ink); line-height: 1; white-space: nowrap; }
  .brand__descriptor {
    font-family: "Arimo", Arial, sans-serif; font-size: 12.4px; color: var(--ink);
    margin-top: 3px; padding-bottom: 5px; border-bottom: 2px dotted var(--ink);
    border-top: 1px dotted var(--ink); padding-top: 2px; white-space: nowrap;
  }

  .tablet { position: absolute; left: 0; top: 0; width: 972px; height: 452px; }
  .screen-caption {
    position: absolute; left: 336px; top: 284px;
    font-family: "Sorts Mill Goudy", Georgia, serif; font-size: 15.5px; color: var(--ink);
    transform: rotate(-6deg); transform-origin: left center; white-space: nowrap;
  }

  .side-label {
    position: absolute; left: 997px; top: 1058px;
    font-family: "Arimo", Arial, sans-serif; font-size: 19px; color: var(--ink);
  }
</style>
</head>
<body>
<main class="stage">

  <section class="flyer flyer--front" aria-label="Vorderseite">
    <h1>
      <span class="headline headline__we">Wir</span>
      <span class="headline headline__congrats">gratulieren zur</span>
      <span class="headline headline__founding">Firmengründung!</span>
    </h1>
    <div class="photo photo--cork-front" role="img" aria-label="Foto eines Sektkorkens mit Drahtkorb und grüner Kappe"></div>
    <div class="band">
      <p class="band__question">Haben Sie steuerliche Fragen?</p>
    </div>
    <div class="brand">
      <div class="brand__name">zahlenkompass.de</div>
      <div class="brand__descriptor">STEUERBERATUNGSGESELLSCHAFT MBH</div>
    </div>
  </section>

  <section class="flyer flyer--back" aria-label="Rückseite">
    <svg class="tablet" viewBox="0 0 972 452">
      <polygon role="img" aria-label="Tablet-Gerät, schräg gestellt" points="66,25 741,-69 788,439 120,533" fill="var(--tablet-dark)"/>
      <polygon points="131,63 683,-18 723,345 178,453" fill="var(--paper)"/>
      <rect role="img" aria-label="Sektkorken mit Mauszeiger auf dem Bildschirm" x="318" y="128" width="216" height="138" rx="40" fill="var(--cork)" opacity="0.55"/>
    </svg>
    <p class="screen-caption">Einfach nach der Feier reinklicken!</p>
    <div class="band">
      <div class="band__contact">
        <p class="band__address">Lindenallee 12<br>20100 Hamburg</p>
        <p class="band__reach">Tel.: 040/123 456 780<br>&nbsp;E-Mail: hamburg@zahlenkompass.de</p>
      </div>
    </div>
    <div class="brand brand--back">
      <div class="brand__name">zahlenkompass.de</div>
      <div class="brand__descriptor">STEUERBERATUNGSGESELLSCHAFT MBH</div>
    </div>
  </section>

  <p class="side-label">Rückseite</p>
</main>
</body>
</html>
```